Design some Business Card for shipping company

We need a creative business card designed for a shipping company. All relevant information such as address and phone number can be found on our website. Will need a design for both front and back. The front will container our logo, slogan, contact information etc. The back will have a coupon and some text. check out www.taldovefreight.example for all the information. We need something memorable and unique that will stand out. It needs to a horizontal design. Not vertical.

```html
<!DOCTYPE html>
<html lang="en">
<head>
<meta charset="utf-8">
<title>Taldove Freight – Business Card</title>
<link href="https://fonts.googleapis.com/css2?family=Arimo:ital,wght@0,400;0,700;1,400&display=swap" rel="stylesheet">
<style>
  :root{
    --bg:#efe9df;
    --card-white:#ffffff;
    --red:#d3222f;
    --red-dark:#a9141f;
    --green:#1f9a3f;
    --ink:#2a2a2a;
  }
  *{margin:0;padding:0;box-sizing:border-box}
  html,body{width:1200px;height:1023px;overflow:hidden;background:var(--bg);font-family:"Arimo",Arial,sans-serif}
  .card{position:absolute;width:660px;height:377px;border-radius:22px;overflow:hidden;box-shadow:0 10px 28px rgba(0,0,0,.22)}
  .card--front{left:60px;top:70px;background:var(--card-white)}
  .card--back{left:480px;top:560px;background:linear-gradient(135deg,#de2b37,var(--red-dark))}
  .front-shapes{position:absolute;inset:0}
  .brand{position:absolute;display:flex;align-items:center;gap:12px}
  .brand__mark{width:34px;height:34px;border-radius:50%;flex:none}
  .brand__name{font-weight:700;font-size:24px;letter-spacing:.5px;text-transform:uppercase;line-height:1;white-space:nowrap}
  .brand__slogan{font-weight:700;font-size:12px;margin-top:5px;white-space:nowrap}
  .card--front .brand{left:110px;top:118px}
  .card--front .brand__mark{background:var(--red)}
  .card--front .brand__name,.card--front .brand__slogan{color:var(--ink)}
  .tagline{position:absolute;right:22px;top:172px;color:#fff;font-size:15px;white-space:nowrap}
  .person{position:absolute;left:40px;top:218px}
  .person__name{font-size:30px;font-weight:700;color:var(--ink)}
  .person__role{font-size:16px;color:var(--red);margin-top:4px}
  .contacts{position:absolute;left:40px;top:282px;list-style:none;font-size:13px;color:var(--ink)}
  .contacts li{display:flex;align-items:center;gap:9px;height:16px;white-space:nowrap}
  .contacts svg{width:12px;height:12px;flex:none}
  .card--back .brand{left:70px;top:62px}
  .card--back .brand__mark{background:#fff}
  .card--back .brand__name{font-size:27px}
  .card--back .brand__slogan{font-size:12.5px}
  .card--back .brand__name,.card--back .brand__slogan{color:#fff}
  .blurb{position:absolute;left:70px;top:160px;width:520px;color:#fff;font-style:italic;font-size:16.5px;line-height:1.45}
</style>
</head>
<body>
  <section class="card card--front">
    <svg class="front-shapes" viewBox="0 0 660 377" aria-hidden="true">
      <path d="M505 0 H660 V377 H235 C355 345 435 260 462 160 C480 90 505 35 505 0Z" fill="var(--red)"/>
      <path d="M222 377 C342 342 422 258 448 165" fill="none" stroke="var(--green)" stroke-width="12"/>
      <path d="M0 362 H180 L172 377 H0Z" fill="var(--red)"/>
    </svg>
    <div class="brand">
      <span class="brand__mark"></span>
      <div><div class="brand__name">Taldove Freight</div><div class="brand__slogan">Secure Affordable Shipping to Kenya</div></div>
    </div>
    <div class="tagline">USA to KENYA shipping</div>
    <div class="person">
      <div class="person__name">Arlen Brooks</div>
      <div class="person__role">Managing Director</div>
    </div>
    <ul class="contacts">
      <li><svg viewBox="0 0 12 12"><path d="M2 1l3 2-1 2 3 3 2-1 2 3-2 1C5 11 1 7 1 3z" fill="var(--green)"/></svg>usa &nbsp;&nbsp;&nbsp;+1 555 014 2270</li>
      <li><svg viewBox="0 0 12 12"><rect x="3" y="1" width="6" height="10" rx="1" fill="none" stroke="var(--green)" stroke-width="1.4"/></svg>kenya +254 700 000 118</li>
      <li><svg viewBox="0 0 12 12"><rect x="1" y="2" width="10" height="8" fill="var(--green)"/><path d="M1 2l5 4 5-4" stroke="#fff" fill="none"/></svg>info@taldovefreight.example</li>
      <li><svg viewBox="0 0 12 12"><circle cx="6" cy="6" r="5" fill="var(--green)"/></svg>www.taldovefreight.example</li>
    </ul>
  </section>

  <section class="card card--back">
    <div class="brand">
      <span class="brand__mark"></span>
      <div><div class="brand__name">Taldove Freight</div><div class="brand__slogan">Secure Affordable Shipping to Kenya</div></div>
    </div>
    <p class="blurb">Fast, secure and reliable ocean shipping service to Kenya from the USA. Our rates include customs and duty all the way to our warehouse in Nairobi. Packages are picked up from our Mombasa rd warehouse. Door to door delivery also available. All prices are based on volume. Weight does not matter. Free package pick up in the Seattle area</p>
  </section>
</body>
</html>
```